Law Firm Website, easily updated by User

We are a regional Labor and Employment Law Firm with a tired outdated website. We are looking for a clean easy to use website that will allow us to easily update information and articles in house. Our current website can be found at www.quillbrookcounsel.com

Industry/Entity Type

Labor

Number of Pages Required

5+ page

Colors
0655a3

Requirements
Must have
• Content easily updated by user
Nice to have
• crisp clean pages
Should not have
• stock pictures

```html
<!DOCTYPE html>
<html lang="en">
<head>
<meta charset="utf-8">
<title>Quillbrook &amp; Partners, P.C.</title>
<link href="https://fonts.googleapis.com/css2?family=Open+Sans:wght@300;400;600;700&family=Tinos&display=swap" rel="stylesheet">
<style>
:root{
  --navy:#13307a;
  --navy-deep:#0f2a6b;
  --navy-bottom:#0c2460;
  --blue:#2b7fc8;
  --blue-light:#3d92d8;
  --btn:#2679c2;
  --ink:#333;
  --muted:#777;
  --line:#d6d6d6;
  --link:#9cc4f2;
  --white:#fff;
}
*{box-sizing:border-box;margin:0;padding:0}
html,body{width:1019px;height:1200px;overflow:hidden;background:var(--white)}
body{position:relative;font-family:"Open Sans",sans-serif;color:var(--ink)}
.abs{position:absolute}

/* header */
.brand{left:84px;top:14px;display:flex;align-items:center;gap:8px}
.brand-mark{width:22px;height:22px;background:var(--navy)}
.brand-name{font-family:"Tinos",serif;font-size:20px;color:#111;line-height:1}
.brand-sub{left:114px;top:44px;font-family:"Tinos",serif;font-size:6.2px;color:#222;letter-spacing:.1px;text-transform:uppercase}
.nav{top:28px;left:400px;width:535px;display:flex;justify-content:space-between;font-size:11px;color:#555}

/* hero */
.hero{left:0;top:65px;width:1019px;height:485px;background:linear-gradient(90deg,#3a3a3a 0%,#8a8a8a 25%,#6b6b6b 45%,#5a5a5a 60%,#3e3e3e 80%,#5c5c5c 100%)}
.hero-title{left:534px;top:245px;color:var(--white);font-size:18.5px;font-weight:700;letter-spacing:.3px}
.hero-sub{left:534px;top:271px;color:var(--white);font-size:22px;font-weight:300;letter-spacing:.2px}
.call-icon{left:536px;top:313px;width:44px;height:44px;background:var(--navy-bottom);display:flex;align-items:center;justify-content:center}
.call-1{left:592px;top:318px;color:var(--white);font-size:12.5px;font-weight:600}
.call-2{left:592px;top:337px;color:var(--white);font-size:14.5px;font-weight:700}
.slide-arrow{top:408px;width:20px;height:22px;background:rgba(90,90,90,.55);display:flex;align-items:center;justify-content:center}

/* feature cards */
.card{top:441px;width:275px;height:145px;padding:22px 24px;color:var(--white);box-shadow:0 10px 10px -6px rgba(0,0,0,.35)}
.card.dark{background:linear-gradient(180deg,#1a3a8a,#18408f)}
.card.light{background:linear-gradient(180deg,#2b77c9,#3a93dc)}
.card h2{font-size:17px;font-weight:700;letter-spacing:.3px;margin-bottom:8px}
.card p{font-size:9.5px;line-height:20px;padding-left:1px}
.card .btn{display:inline-block;margin-top:10px;border:1px solid var(--white);font-size:7.5px;padding:7px 14px;border-radius:2px}

/* about */
.h3{font-size:12px;font-weight:700;color:#333;letter-spacing:.1px}
.about-photo{left:84px;top:670px;width:203px;height:111px;background:linear-gradient(90deg,#4a2f22,#7a5a45 60%,#5a3b2a)}
.about-text{color:var(--muted);font-size:9.2px;line-height:19px}
.read-more{left:84px;top:850px;width:126px;height:34px;background:var(--btn);color:var(--white);font-size:10.5px;font-weight:700;display:flex;align-items:center;justify-content:center;border-radius:2px}

/* faq */
.faq-item{left:683px;width:252px;border:1px solid var(--line);font-size:8.6px;color:#444;display:flex;justify-content:space-between;align-items:center;padding:0 9px 0 13px;height:32px}
.faq-answer{left:688px;top:709px;width:240px;font-size:9.2px;line-height:18.5px;color:var(--muted)}
.faq-answer span{color:var(--navy);font-weight:600}

/* footer */
.footer{left:0;top:935px;width:1019px;height:219px;background:var(--navy-deep)}
.footer h4{font-size:11.5px;font-weight:700;color:var(--white);letter-spacing:.2px}
.footer ul{list-style:none;margin-top:12px}
.footer li{font-size:9.3px;color:var(--link);line-height:21.2px}
.badge{left:781px;top:966px;width:86px;height:64px;background:var(--white);border-radius:4px;overflow:hidden}
.badge i{position:absolute;left:0;bottom:0;width:100%;height:12px;background:#f07d1a}
.social{left:782px;top:1078px;display:flex;gap:9px}
.social span{width:23px;height:23px;border-radius:50%;background:#2a4a98}
.bottom{left:0;top:1154px;width:1019px;height:46px;background:var(--navy-bottom);display:flex;align-items:center;justify-content:center;gap:14px;font-size:9.5px;color:var(--link)}
</style>
</head>
<body>

<header>
  <div class="abs brand"><span class="brand-mark"></span><span class="brand-name">Quillbrook &amp; Partners, P.C.</span></div>
  <div class="abs brand-sub">Employment Counseling, Litigation, Labor &amp; Benefits Law</div>
  <nav class="abs nav">
    <span>Attorneys</span><span>Practice Areas</span><span>FAQ</span><span>In the News</span><span>For Employers</span><span>Contact Us</span>
  </nav>
</header>

<section class="abs hero" role="img" aria-label="Black and white photo of a team of attorneys in business suits"></section>
<div class="abs hero-title">COUNSELING AND ADVISING CLIENTS</div>
<div class="abs hero-sub">EXCLUSIVELY ON LAWS OF THE WORKPLACE</div>
<div class="abs call-icon">
  <svg width="20" height="20" viewBox="0 0 24 24"><path fill="#fff" d="M6.6 10.8a15.1 15.1 0 0 0 6.6 6.6l2.2-2.2a1 1 0 0 1 1-.25 11.4 11.4 0 0 0 3.6.57 1 1 0 0 1 1 1V20a1 1 0 0 1-1 1A17 17 0 0 1 3 4a1 1 0 0 1 1-1h3.5a1 1 0 0 1 1 1c0 1.25.2 2.45.57 3.57a1 1 0 0 1-.25 1z"/></svg>
</div>
<div class="abs call-1">FOR A FREE CONSULTATION</div>
<div class="abs call-2">CALL (555) 014-2290</div>
<div class="abs slide-arrow" style="left:893px"><svg width="8" height="10" viewBox="0 0 8 10"><path d="M6 1 2 5l4 4" stroke="#ccc" fill="none" stroke-width="1.2"/></svg></div>
<div class="abs slide-arrow" style="left:915px"><svg width="8" height="10" viewBox="0 0 8 10"><path d="M2 1l4 4-4 4" stroke="#ccc" fill="none" stroke-width="1.2"/></svg></div>

<div class="abs card dark" style="left:84px"><h2>PRACTICE AREAS</h2><p>Our attorneys provide a diverse range of counseling and training in areas of the law...</p><span class="btn">CLICK HERE</span></div>
<div class="abs card light" style="left:372px"><h2>FOR EMPLOYERS</h2><p>Our attorneys provide a diverse range of counseling and training in areas of the law...</p><span class="btn">CLICK HERE</span></div>
<div class="abs card light" style="left:659px"><h2>ATTORNEYS</h2><p>Our attorneys provide a diverse range of counseling and training in areas of the law...</p><span class="btn">CLICK HERE</span></div>

<h3 class="abs h3" style="left:84px;top:634px">ABOUT QUILLBROOK &amp; PARTNERS, P.C.</h3>
<div class="abs about-photo" role="img" aria-label="Photo of an attorney in a robe seated beside a stack of law books"></div>
<p class="abs about-text" style="left:311px;top:667px;width:345px">Es simplemente el texto de relleno de las imprentas y archivos de texto. Lorem Ipsum ha sido el texto de relleno estándar de las industrias desde el año 1500, cuando un impresor (N. del T. persona que se dedica a la imprenta) desconocido usó una galería de textos y los mezcló de tal manera que logró hacer un libro de textos especimen. No sólo sobrevivió 500 años, sino que tambien ingresó como texto de relleno en documentos electrónicos.</p>
<p class="abs about-text" style="left:84px;top:797px;width:575px">Es simplemente el texto de relleno de las imprentas y archivos de texto. Lorem Ipsum ha sido el texto de relleno estándar de las industrias desde el año 1500, cuando un impresor desconocido usó una galería de textos y los mezcló de tal...</p>
<div class="abs read-more">READ MORE INFO</div>

<h3 class="abs h3" style="left:681px;top:634px">FREQUENTLY ASKED QUESTIONS</h3>
<div class="abs faq-item" style="top:663px"><span>DISCRIMINATION/CIVIL RIGHTS ACTS/TITLE VII</span><span>[ - ]</span></div>
<p class="abs faq-answer">Federal and state laws prohibit employment practices (such as hiring, discharge, promotions and pay) which are based upon an individual's race, color, religion, national origin &nbsp;<span>[ Read more ]</span></p>
<div class="abs faq-item" style="top:795px"><span>SEXUAL HARASSMENT</span><span>[ + ]</span></div>
<div class="abs faq-item" style="top:830px"><span>AGE DISCRIMINATION (ADEA) &amp; OLDER WORKER...</span><span>[ + ]</span></div>
<div class="abs faq-item" style="top:860px"><span>WAGE/HOUR REQUIREMENTS</span><span>[ + ]</span></div>

<footer>
  <div class="abs footer"></div>
  <div class="abs footer" style="background:none;height:auto;left:84px;top:966px;width:300px">
    <h4>ADMISSIONS</h4>
    <ul><li>New York State</li><li>Eastern District of New York</li><li>Southern District of New York</li><li>United States Court of Appeals for the Second Circuit</li><li>United States Court of Federal Claims</li><li>United States Supreme Court</li></ul>
  </div>
  <div class="abs footer" style="background:none;height:auto;left:383px;top:966px;width:250px">
    <h4>ASSOCIATIONS</h4>
    <ul><li>Empire State Bar Guild</li><li>Harbor County Bar Guild</li><li>Eastshore County Bar Guild</li><li>National Trial Counsel Society</li><li>Workplace Advocates Alliance</li></ul>
  </div>
  <div class="abs footer" style="background:none;height:auto;left:659px;top:966px;width:120px">
    <h4>WELCOME</h4>
    <ul><li>Contact Us</li><li>Attorneys</li><li>Practice Areas</li><li>FAQ</li><li>In the News</li><li>For Employers</li></ul>
  </div>
  <div class="abs badge"><i></i></div>
  <h4 class="abs" style="left:782px;top:1052px;font-size:11.5px;font-weight:700;color:#fff">FOLLOW US</h4>
  <div class="abs social"><span></span><span></span><span></span><span></span><span></span></div>
  <div class="abs bottom"><span>Copyright © 2015. All Rights Reserved. Quillbrook &amp; Partners, P.C.</span><span>/</span><span>Privacy Policy</span><span>/</span><span>Disclaimer</span></div>
</footer>

</body>
</html>
```